Business Card for Bright Meadow Lawn & Landscape

Double Sided Card Design - I think one side of the card should be cleaner, with logo, contact info, and "Complete Residential & Commercial Landscape Services", and on the other side it should list the services we offer:

- Lawn Care & Mowing
- Hedge & Shrub Trimming
- Leaf Removal & Clean Up
- Aeration & Sod
- Mulch & Rock Installations
- Landscape Installations & Renovations
- Commercial Snow Removal

Please make it clean and very professional... don't want it too be too busy, but want to tell them what we do.

Target Market(s)

Residential and Commercial

Industry/Entity Type

Landscape

Contact Information for Business Card

Fully Insured
Tom Berrigan
410-555-0198
Tberrigan07@mailbox-example.com

Requirements
Must have
• Double Sided, Cleaner on one side, more information and text on the other side.

```html
<!DOCTYPE html>
<html lang="en">
<head>
<meta charset="utf-8">
<title>Bright Meadow Lawn &amp; Landscape – Business Card</title>
<link rel="stylesheet" href="https://fonts.googleapis.com/css2?family=Lato:ital,wght@0,400;0,700;1,400&display=swap">
<style>
  :root {
    --backdrop: #e9e6e1;
    --card-black: #050505;
    --leaf-green: #6cb33f;
    --leaf-green-dark: #3f7d1f;
    --text-white: #f4f4f4;
    --rule-green: #6cb33f;
  }
  * { box-sizing: border-box; margin: 0; padding: 0; }
  html, body {
    width: 1200px; height: 800px; overflow: hidden;
    background: var(--backdrop);
    font-family: "Lato", Arial, sans-serif;
  }
  .stage { position: relative; width: 1200px; height: 800px; }
  .card {
    position: absolute; top: 245px;
    width: 540px; height: 310px;
    background: var(--card-black);
    overflow: hidden;
    box-shadow: 0 10px 24px rgba(0,0,0,.25);
    color: var(--text-white);
  }
  .card--services { left: 40px; }
  .card--contact { left: 620px; }

  /* Services side */
  .service-list { position: absolute; left: 44px; top: 62px; list-style: none; }
  .service-list li {
    display: flex; align-items: center; gap: 12px;
    font-size: 17px; line-height: 27px; letter-spacing: .2px;
  }
  .tick { width: 16px; height: 14px; flex: none; }
  .brand-mark {
    position: absolute; right: 38px; top: 40px;
    width: 150px; display: flex; flex-direction: column; align-items: center; gap: 10px;
    text-align: center;
  }
  .brand-dot { width: 96px; height: 96px; border-radius: 50%; background: var(--leaf-green); }
  .brand-name { color: var(--leaf-green); font-weight: 700; font-size: 15px; line-height: 1.25; }
  .accent-band { position: absolute; left: 0; bottom: 0; width: 540px; height: 90px; }

  /* Contact side */
  .brand-lockup {
    position: absolute; left: 34px; top: 62px; width: 220px;
    display: flex; flex-direction: column; align-items: center; gap: 10px; text-align: center;
  }
  .brand-lockup .brand-dot { width: 56px; height: 56px; }
  .brand-lockup .brand-name { font-size: 20px; line-height: 1.2; }
  .divider { position: absolute; left: 278px; top: 62px; width: 2px; height: 130px; background: var(--rule-green); }
  .contact { position: absolute; left: 300px; top: 82px; }
  .contact-name { color: var(--leaf-green); font-size: 24px; font-weight: 400; margin-bottom: 24px; }
  .contact-line { font-size: 14.5px; line-height: 22px; }
  .insured {
    position: absolute; left: 0; right: 0; top: 218px; text-align: center;
    color: var(--leaf-green); font-style: italic; font-size: 15px;
  }
  .tagline {
    position: absolute; left: 0; right: 0; top: 240px; text-align: center;
    font-size: 16px; letter-spacing: .2px;
  }
  .grass-corner {
    position: absolute; width: 58px; height: 50px;
    background: linear-gradient(to top, var(--leaf-green-dark), var(--leaf-green) 60%, transparent);
    opacity: .85;
  }
  .grass-corner--left { left: 0; bottom: 0; }
  .grass-corner--right { right: 0; bottom: 0; }
</style>
</head>
<body>
<main class="stage">

  <section class="card card--services" aria-label="Card back: services">
    <ul class="service-list">
      <li><svg class="tick" viewBox="0 0 16 14"><path d="M1 7l5 5L15 1" fill="none" stroke="var(--leaf-green)" stroke-width="2.4"/></svg>Lawn Care &amp; Mowing</li>
      <li><svg class="tick" viewBox="0 0 16 14"><path d="M1 7l5 5L15 1" fill="none" stroke="var(--leaf-green)" stroke-width="2.4"/></svg>Hedge &amp; Shrub Trimming</li>
      <li><svg class="tick" viewBox="0 0 16 14"><path d="M1 7l5 5L15 1" fill="none" stroke="var(--leaf-green)" stroke-width="2.4"/></svg>Leaf Removal &amp; Clean Up</li>
      <li><svg class="tick" viewBox="0 0 16 14"><path d="M1 7l5 5L15 1" fill="none" stroke="var(--leaf-green)" stroke-width="2.4"/></svg>Aeration &amp; Sod</li>
      <li><svg class="tick" viewBox="0 0 16 14"><path d="M1 7l5 5L15 1" fill="none" stroke="var(--leaf-green)" stroke-width="2.4"/></svg>Mulch &amp; Rock Installations</li>
      <li><svg class="tick" viewBox="0 0 16 14"><path d="M1 7l5 5L15 1" fill="none" stroke="var(--leaf-green)" stroke-width="2.4"/></svg>Landscape Installations &amp; Renovations</li>
      <li><svg class="tick" viewBox="0 0 16 14"><path d="M1 7l5 5L15 1" fill="none" stroke="var(--leaf-green)" stroke-width="2.4"/></svg>Commercial Snow Removal</li>
    </ul>
    <div class="brand-mark">
      <span class="brand-dot"></span>
      <span class="brand-name">Bright Meadow Lawn &amp; Landscape</span>
    </div>
    <svg class="accent-band" viewBox="0 0 540 90" preserveAspectRatio="none">
      <polygon points="0,78 540,18 540,32 0,90" fill="var(--leaf-green)"/>
    </svg>
  </section>

  <section class="card card--contact" aria-label="Card front: contact">
    <div class="brand-lockup">
      <span class="brand-dot"></span>
      <span class="brand-name">Bright Meadow Lawn &amp; Landscape</span>
    </div>
    <div class="divider"></div>
    <div class="contact">
      <p class="contact-name">Tom Berrigan</p>
      <p class="contact-line">410-555-0198</p>
      <p class="contact-line">Tberrigan07@mailbox-example.com</p>
    </div>
    <p class="insured">Fully Insured</p>
    <p class="tagline">Complete Residential &amp; Commercial Landscape Services</p>
    <div class="grass-corner grass-corner--left" role="img" aria-label="Green grass blades decoration"></div>
    <div class="grass-corner grass-corner--right" role="img" aria-label="Green grass blades decoration"></div>
  </section>

</main>
</body>
</html>
```